International game business needs app design

We are planning to release a new mobile game on Qbe5 which requires a fresh, flat, reduced and functional design, fulfilling Brindle’s Qbe5 design guidelines
.
The design shall be created for a dashboard, where players should be able to pick levels (icon + short description; 300+ levels), opponents (icon/photo/avatar image + short description; 5-100) and read/delete system/chat messages (icon, 2-3 actions (delete, accept/decline), text with up to 500 characters; 1-100 entries), Menu bar (settings, shop, leaderboards, achievements, and one or two more menu items) It must consider means to search/select levels and opponents. Would be nice to have an option to start playing immediately (with a random opponent on a random level)

Overall Style/Look: fresh, flat, functional, lot’s of free space, warm color scheme. If full screen images are being used it must be considered that there are user-generated photos or avatars which have to work with it in combination

Ideally the design is responsive and would work both on a smartphone and a tablet. Smartphone is top priority, tablet is optional.

The app will be a game for women predominantly, aged 25-35, with higher education and household net income, which should be reflected in color scheme, icons and navigation.

Some of us like flat design, so you might stick to that or impress all of us with something completely new!

The winner will have the chance to design all screens for the app and will have access to a much bigger budget.

UPDATE: A wireframe is attached - but you don't have to follow the depicted layout. Actually it would be highly appreciated if you could come up with something new. The only important thing is that all the listed components must appear somehow on the dashboard.

Target Market(s)

US, AU, NZ, GB, CA

Industry/Entity Type

Education

Colors

Designer to choose colors to be used in the design.

Requirements
Must have
• All the functional components described above.
Design must be in line with Qbe5 design guidelines https://makers.brindlehub.example/library/qbe/documentation/UserExperience/Conceptual/TouchGuide/index.html
Nice to have
• We would like to have someone with the following attributes:
* minimum 5 qbe design in your past at least 2 of them responsive – please provide links to the apps you created
* besides UI designer skills would be nice you to have UX skills

The most important factors for us are quality, creativity, speed, flexibility (“be able to take criticism into account”)
Should not have
• We don’t want a girly design so please don’t use too much pinks, flowers and such. The design should be acceptable by men too.

```html
<!DOCTYPE html>
<html lang="en">
<head>
<meta charset="utf-8">
<title>Game Dashboard</title>
<link href="https://fonts.googleapis.com/css2?family=Open+Sans:wght@400;600;700&display=swap" rel="stylesheet">
<style>
:root{
  --status-bg:#2c2b33;
  --nav-bg:#47415f;
  --nav-icon:#8c86ab;
  --accent:#f4456a;
  --card-dark:#3f3a59;
  --pill-grey:#c8c8c8;
  --panel-bg:#ebebeb;
  --white:#ffffff;
  --text-dark:#3a3a3a;
  --text-muted:#a8a8a8;
  --line:#e4e4e4;
  --title-purple:#5a5480;
}
*{margin:0;padding:0;box-sizing:border-box}
html,body{width:1200px;height:2163px;overflow:hidden;background:var(--panel-bg);font-family:"Open Sans",sans-serif}
.screen{position:relative;width:1200px;height:2163px;overflow:hidden;background:var(--panel-bg)}
.status-bar{position:absolute;left:0;top:0;width:1200px;height:66px;background:var(--status-bg);color:var(--white);font-weight:700;font-size:44px;display:flex;align-items:center;padding:0 24px}
.status-bar .carrier{display:flex;align-items:center;gap:12px}
.status-bar .time{position:absolute;left:0;right:0;text-align:center}
.status-bar .battery{margin-left:auto;display:flex;align-items:center;gap:14px}
.nav-bar{position:absolute;left:0;top:66px;width:1200px;height:120px;background:var(--nav-bg);display:flex;justify-content:space-around;align-items:center;padding:0 90px}
.nav-bar svg{width:56px;height:56px}
.top-area{position:absolute;left:0;top:186px;width:1200px;height:519px;background:linear-gradient(110deg,#e9e9ea 0%,#fafafa 40%,#e4e4e6 100%)}
.tabs{position:absolute;top:32px;left:0;width:1200px}
.tab{position:absolute;height:54px;width:245px;border-radius:27px;background:var(--pill-grey);color:var(--white);font-size:25px;display:flex;align-items:center;justify-content:center;text-transform:uppercase}
.tab.active{background:var(--accent)}
.levels{position:absolute;top:167px;left:0;width:1200px;height:149px}
.level-card{position:absolute;top:0;width:216px;height:149px;background:var(--card-dark);border-radius:6px;color:var(--white);text-align:center}
.level-card.current{background:var(--accent)}
.level-card .name{font-size:22px;margin-top:8px}
.level-card .num{font-size:60px;font-weight:600;line-height:64px}
.level-card .label{font-size:20px;text-transform:uppercase}
.level-arrow{position:absolute;top:48px;width:32px;height:52px}
.search{position:absolute;top:404px;left:48px;width:1092px;height:80px;background:var(--white);border-radius:10px;color:var(--text-muted);font-size:33px;display:flex;align-items:center;justify-content:center}
.search svg{position:absolute;right:30px;top:18px;width:46px;height:46px}
.opponents{position:absolute;left:0;top:705px;width:1200px;height:442px;background:linear-gradient(100deg,#c7a8a8 0%,#e6d4cc 25%,#b9b0b5 50%,#d8c9c3 75%,#c9bcb4 100%)}
.opponent{position:absolute;top:36px;width:290px;text-align:center}
.opponent .photo{width:284px;height:284px;margin:0 auto;border-radius:50%;border:7px solid var(--white);background:radial-gradient(circle at 50% 40%,#c99d86 0%,#8a7167 55%,#5b5050 100%)}
.opponent .name{display:inline-block;margin-top:-26px;position:relative;background:var(--white);border-radius:22px;padding:4px 34px;font-size:27px;color:var(--text-dark);min-width:230px}
.opponent .actions{display:flex;justify-content:center;gap:26px;margin-top:26px}
.opponent .actions svg{width:44px;height:44px}
.messages{position:absolute;left:24px;top:1186px;width:1152px;height:751px;background:var(--white)}
.messages-head{height:142px;display:flex;align-items:center;padding-left:40px;border-bottom:2px solid var(--line);position:relative}
.messages-head h2{font-weight:400;font-size:34px;color:var(--title-purple);margin-left:34px}
.messages-head .close{position:absolute;right:22px;top:14px;width:40px;height:40px;background:#c4c4c4;display:flex;align-items:center;justify-content:center}
.message{height:116px;display:flex;align-items:center;padding-left:36px;border-bottom:2px solid var(--line);position:relative}
.message:last-child{border-bottom:none}
.avatar{width:72px;height:72px;border-radius:50%;border:3px solid #eee;background:radial-gradient(circle at 50% 40%,#e1a98c,#8e5e4a)}
.avatar.teal{background:radial-gradient(circle at 50% 40%,#e8c2a9,#5fae9e)}
.message .who{margin-left:48px;font-size:36px;font-weight:600;color:var(--text-dark)}
.message .note{font-size:24px;font-weight:400;color:#888;margin-left:12px}
.message .action{position:absolute;left:880px;display:flex;align-items:center;gap:28px;font-size:25px;color:var(--text-muted)}
.message .action svg{width:50px;height:40px}
.play-button{position:absolute;left:89px;top:1985px;width:1008px;height:122px;background:var(--accent);color:var(--white);font-size:50px;font-weight:700;display:flex;align-items:center;justify-content:center;border-radius:3px}
</style>
</head>
<body>
<div class="screen">

  <header class="status-bar">
    <div class="carrier">
      <svg width="70" height="34" viewBox="0 0 70 34" aria-hidden="true">
        <rect x="0" y="22" width="9" height="12" fill="#fff"/><rect x="14" y="16" width="9" height="18" fill="#fff"/>
        <rect x="28" y="10" width="9" height="24" fill="#fff"/><rect x="42" y="5" width="9" height="29" fill="#fff"/>
        <rect x="56" y="0" width="9" height="34" fill="#fff"/>
      </svg>
      <span>LUNE</span>
    </div>
    <div class="time">10:35 AM</div>
    <div class="battery">
      <svg width="38" height="38" viewBox="0 0 38 38" aria-hidden="true"><circle cx="19" cy="19" r="17" fill="#fff"/><path d="M19 8v12h8" stroke="#2c2b33" stroke-width="4" fill="none"/></svg>
      <span>65%</span>
      <svg width="78" height="38" viewBox="0 0 78 38" aria-hidden="true"><rect x="2" y="4" width="66" height="30" rx="4" fill="none" stroke="#fff" stroke-width="4"/><rect x="8" y="10" width="38" height="18" fill="#fff"/><rect x="70" y="13" width="6" height="12" fill="#fff"/></svg>
    </div>
  </header>

  <nav class="nav-bar">
    <svg viewBox="0 0 24 24" aria-label="Settings"><path fill="var(--nav-icon)" d="M10 1h4l.6 3 2.2 1.2 2.8-1.3 2.8 2.8-1.3 2.8L22.3 11.7l1.7.3v4l-3 .6-1.2 2.2 1.3 2.8-2.8 2.8-2.8-1.3-2.2 1.2L14 23h-4l-.6-3-2.2-1.2-2.8 1.3-2.8-2.8 1.3-2.8L1.7 12.3 0 12V8l3-.6 1.2-2.2L2.9 2.4 5.7-.4 8.5.9 9.4 4z" transform="translate(0 1) scale(.95)"/><circle cx="12" cy="12" r="4" fill="var(--nav-bg)"/></svg>
    <svg viewBox="0 0 24 24" aria-label="Shop"><path fill="var(--nav-icon)" d="M1 3h4l3 12h12l3-9H7l-.6-2H1z"/><circle cx="10" cy="20" r="2" fill="var(--nav-icon)"/><circle cx="18" cy="20" r="2" fill="var(--nav-icon)"/></svg>
    <svg viewBox="0 0 24 24" aria-label="Leaderboards"><path fill="none" stroke="var(--nav-icon)" stroke-width="1.8" d="M5 1h10l4 4v18H5z"/><path stroke="var(--nav-icon)" stroke-width="1.8" d="M8 10h8M8 14h8M8 18h8"/></svg>
    <svg viewBox="0 0 24 24" aria-label="Achievements"><circle cx="12" cy="11" r="5" fill="var(--nav-icon)"/><rect x="10" y="16" width="4" height="4" fill="var(--nav-icon)"/><path stroke="var(--nav-icon)" stroke-width="1.6" d="M12 1v3M3 11h3M18 11h3M5 4l2 2M19 4l-2 2"/></svg>
  </nav>

  <section class="top-area">
    <div class="tabs">
      <div class="tab" style="left:187px">Recent levels</div>
      <div class="tab active" style="left:470px">Choose level</div>
      <div class="tab" style="left:751px">Random</div>
    </div>

    <div class="levels">
      <svg class="level-arrow" style="left:44px" viewBox="0 0 32 52" aria-label="Previous"><path d="M24 6L8 26l16 20" stroke="var(--card-dark)" stroke-width="4" fill="none"/></svg>
      <div class="level-card current" style="left:113px"><div class="name">Hipster wardrobe</div><div class="num">5</div><div class="label">Level</div></div>
      <div class="level-card" style="left:365px"><div class="name">Scribble</div><div class="num">9</div><div class="label">Level</div></div>
      <div class="level-card" style="left:617px"><div class="name">Rock it Now!</div><div class="num">16</div><div class="label">Level</div></div>
      <div class="level-card" style="left:866px"><div class="name">Doing time</div><div class="num">25</div><div class="label">Level</div></div>
      <svg class="level-arrow" style="left:1126px" viewBox="0 0 32 52" aria-label="Next"><path d="M8 6l16 20L8 46" stroke="var(--card-dark)" stroke-width="4" fill="none"/></svg>
    </div>

    <div class="search">search opponent
      <svg viewBox="0 0 24 24" aria-hidden="true"><circle cx="10" cy="10" r="7" fill="none" stroke="#cfcfcf" stroke-width="1.6"/><path d="M15 15l7 7" stroke="#cfcfcf" stroke-width="1.6"/></svg>
    </div>
  </section>

  <section class="opponents" role="img" aria-label="Soft blurred background photo behind the opponent list">
    <div class="opponent" style="left:66px">
      <div class="photo" role="img" aria-label="Opponent profile photo"></div>
      <div class="name">Mara Ellison</div>
      <div class="actions">
        <svg viewBox="0 0 24 24"><path fill="#fff" d="M12 2l3 7h7l-6 4.5 2.3 7.5L12 16.5 5.7 21 8 13.5 2 9h7z"/></svg>
        <svg viewBox="0 0 24 24"><path fill="var(--accent)" d="M12 21l-9-9a5 5 0 017-7l2 2 2-2a5 5 0 017 7z"/></svg>
        <svg viewBox="0 0 24 24"><path fill="#fff" d="M2 3h20v14H9l-5 4v-4H2z"/></svg>
      </div>
    </div>
    <div class="opponent" style="left:450px">
      <div class="photo" role="img" aria-label="Opponent profile photo"></div>
      <div class="name">Theo K</div>
      <div class="actions">
        <svg viewBox="0 0 24 24"><path fill="#fff" d="M12 2l3 7h7l-6 4.5 2.3 7.5L12 16.5 5.7 21 8 13.5 2 9h7z"/></svg>
        <svg viewBox="0 0 24 24"><path fill="#fff" d="M12 21l-9-9a5 5 0 017-7l2 2 2-2a5 5 0 017 7z"/></svg>
        <svg viewBox="0 0 24 24"><path fill="#fff" d="M2 3h20v14H9l-5 4v-4H2z"/></svg>
      </div>
    </div>
    <div class="opponent" style="left:822px">
      <div class="photo" role="img" aria-label="Opponent profile photo"></div>
      <div class="name">Ines R</div>
      <div class="actions">
        <svg viewBox="0 0 24 24"><path fill="#fff" d="M12 2l3 7h7l-6 4.5 2.3 7.5L12 16.5 5.7 21 8 13.5 2 9h7z"/></svg>
        <svg viewBox="0 0 24 24"><path fill="#fff" d="M12 21l-9-9a5 5 0 017-7l2 2 2-2a5 5 0 017 7z"/></svg>
        <svg viewBox="0 0 24 24"><path fill="#fff" d="M2 3h20v14H9l-5 4v-4H2z"/></svg>
      </div>
    </div>
  </section>

  <section class="messages">
    <div class="messages-head">
      <svg width="64" height="60" viewBox="0 0 32 30" aria-hidden="true"><path fill="var(--title-purple)" d="M2 4a9 7 0 0118 0 9 7 0 01-12 6l-5 3 1-4A7 7 0 012 4z"/><path fill="#8c86ab" d="M14 14a8 6 0 0116 2 8 6 0 01-2 5l1 5-5-3a8 6 0 01-10-9z"/></svg>
      <h2>Messages &amp; Notifications</h2>
      <div class="close"><svg width="20" height="20" viewBox="0 0 20 20"><path d="M4 4l12 12M16 4L4 16" stroke="#fff" stroke-width="3"/></svg></div>
    </div>

    <div class="message">
      <div class="avatar" role="img" aria-label="Player avatar"></div>
      <div class="who">Clara Whitfield</div>
      <div class="action"><svg viewBox="0 0 25 20"><rect x="1" y="1" width="23" height="18" fill="none" stroke="#cfcfcf" stroke-width="1.4"/><path d="M1 1l11.5 10L24 1M1 19l8-8M24 19l-8-8" fill="none" stroke="#cfcfcf" stroke-width="1.4"/></svg>open message</div>
    </div>
    <div class="message">
      <div class="avatar" role="img" aria-label="Player avatar"></div>
      <div class="who">Owen Halloway</div>
      <div class="action"><svg viewBox="0 0 25 20"><rect x="1" y="1" width="23" height="18" fill="none" stroke="#cfcfcf" stroke-width="1.4"/><path d="M1 1l11.5 10L24 1M1 19l8-8M24 19l-8-8" fill="none" stroke="#cfcfcf" stroke-width="1.4"/></svg>open message</div>
    </div>
    <div class="message">
      <div class="avatar teal" role="img" aria-label="Player avatar"></div>
      <div class="who">Dana Rivers,<span class="note">just played Scribble. Go join!</span></div>
      <div class="action"><svg viewBox="0 0 25 20"><path d="M3 19V1h18l-4 5 4 5H3" fill="none" stroke="#cfcfcf" stroke-width="1.4"/></svg>notification</div>
    </div>
    <div class="message">
      <div class="avatar" role="img" aria-label="Player avatar"></div>
      <div class="who">Owen Halloway</div>
      <div class="action"><svg viewBox="0 0 25 20"><rect x="1" y="1" width="23" height="18" fill="none" stroke="#cfcfcf" stroke-width="1.4"/><path d="M1 1l11.5 10L24 1M1 19l8-8M24 19l-8-8" fill="none" stroke="#cfcfcf" stroke-width="1.4"/></svg>open message</div>
    </div>
    <div class="message">
      <div class="avatar teal" role="img" aria-label="Player avatar"></div>
      <div class="who">Dana Rivers,<span class="note">just played Scribble. Go join!</span></div>
      <div class="action"><svg viewBox="0 0 25 20"><path d="M3 19V1h18l-4 5 4 5H3" fill="none" stroke="#cfcfcf" stroke-width="1.4"/></svg>notification</div>
    </div>
  </section>

  <div class="play-button">Play a random game</div>
</div>
</body>
</html>
```